I'm an Executive Coach. I need a cover for a leadership book.

Title: Quiet Compass Steady Course Guidance from the Center of the Soul. The focus in my work "Spirit Kindled Reach" I use a lot of fire and heart-centered frame work and imagery. The book should have a leadership presence with an inspirational feel. The purpose is to invite really smart leaders to pay attention and to lead from their heart so they can have great impact in the work they do and the lives they live. paxtonlowry.example to see site branding, colors. Author: Paxton Lowry

Target Market(s)

The audience is those lead others from the manager level to the executive level and entrepreneurs starting and leading their own companies They are usually trailblazers, care about connecting with people as they lead. The big message is being confifent to lead ftom values, intention and from what matters most.

Industry/Entity Type

Executive coaching

Font styles to use
Serif

Requirements
Must have
• Lighter feel. Perhaps avoid a total black background.
Nice to have
• While it is a leadership book, i would like it to feel creative and inviting not authoritative.
Should not have
• Dark colors as the main color

```html
<!DOCTYPE html>
<html lang="en">
<head>
<meta charset="utf-8">
<title>Quiet Compass Steady Course — Paxton Lowry</title>
<link rel="stylesheet" href="https://fonts.googleapis.com/css2?family=Playfair+Display:wght@400;700&family=Allura&display=swap">
<style>
  :root {
    --page-bg: #e6e6e6;
    --blush: #f6e2d8;
    --peach: #eec1ab;
    --rose: #d99a8c;
    --coral: #c9786a;
    --amber-glow: rgba(240, 170, 110, 0.75);
    --ink-wine: #4a1f2e;
    --ink-soft: #6b3242;
    --rule: rgba(74, 31, 46, 0.35);
    --band: #f4f1ee;
    --signature: #a8384a;
    --heart-core: #9a4350;
    --flame: #f2a33a;
  }
  * { margin: 0; padding: 0; box-sizing: border-box; }
  html, body {
    width: 1014px;
    height: 1200px;
    overflow: hidden;
    background: var(--page-bg);
  }
  .cover {
    position: absolute;
    left: 120px;
    top: 20px;
    width: 774px;
    height: 1160px;
    overflow: hidden;
    display: flex;
    flex-direction: column;
    background:
      radial-gradient(ellipse 50% 35% at 12% 2%, var(--amber-glow), transparent 70%),
      radial-gradient(ellipse 60% 40% at 95% 5%, rgba(217, 154, 140, 0.8), transparent 75%),
      radial-gradient(ellipse 55% 45% at 50% 70%, rgba(240, 180, 140, 0.6), transparent 75%),
      linear-gradient(180deg, var(--blush) 0%, var(--peach) 45%, var(--rose) 100%);
  }
  .cover__body {
    position: relative;
    flex: 1;
    text-align: center;
    color: var(--ink-wine);
    font-family: "Playfair Display", Georgia, serif;
    padding-top: 96px;
  }
  .title { font-weight: 700; }
  .title__line {
    display: block;
    font-size: 68px;
    line-height: 84px;
    letter-spacing: 0.5px;
  }
  .title__tagline {
    display: block;
    margin-top: 10px;
    font-size: 32px;
    font-weight: 400;
    letter-spacing: 2px;
    line-height: 40px;
    color: var(--ink-soft);
  }
  .subtitle {
    width: 435px;
    margin: 30px auto 0;
    padding: 12px 0 14px;
    border-top: 1px solid var(--rule);
    border-bottom: 1px solid var(--rule);
    font-size: 34px;
    font-style: italic;
    line-height: 44px;
    color: var(--ink-wine);
  }
  .heart-art {
    position: absolute;
    left: 230px;
    top: 520px;
    width: 320px;
    height: 470px;
    border-radius: 45% 45% 48% 48%;
    background:
      radial-gradient(ellipse 48% 52% at 52% 58%, var(--heart-core) 0%, #b85a5e 45%, rgba(242, 163, 58, 0.6) 75%, transparent 100%);
  }
  .author-band {
    height: 130px;
    background: var(--band);
    display: flex;
    align-items: center;
    justify-content: center;
  }
  .author-band__name {
    font-family: "Allura", cursive;
    font-size: 86px;
    color: var(--signature);
    line-height: 1;
    padding-top: 6px;
  }
</style>
</head>
<body>
  <main class="cover">
    <section class="cover__body">
      <h1 class="title">
        <span class="title__line">QUIET COMPASS</span>
        <span class="title__line">STEADY COURSE</span>
        <span class="title__tagline">PERSONAL &amp; PROFESSIONAL</span>
      </h1>
      <p class="subtitle">Guidance from the<br>Center of the Soul</p>
      <div class="heart-art" role="img" aria-label="Illustration of an anatomical heart wrapped in glowing flames"></div>
    </section>
    <footer class="author-band">
      <p class="author-band__name">Paxton Lowry</p>
    </footer>
  </main>
</body>
</html>
```